Business Card Design for Kestrelwood Carpentry

I need a business card design for my carpentry company Kestrelwood Carpentry. Ive attached files with all information I require on both sides. Look forward to seeing your design.

```html
<!DOCTYPE html>
<html lang="en">
<head>
<meta charset="utf-8">
<title>Kestrelwood Carpentry – Business Card</title>
<link href="https://fonts.googleapis.com/css2?family=Saira:wght@500;700;800&display=swap" rel="stylesheet">
<style>
  :root {
    --orange: #ee5a24;
    --orange-soft: #fbe3d6;
    --ink: #2b2b2b;
    --white: #ffffff;
    --backdrop: #e9e9e9;
    --grey-soft: #e4e4e4;
  }
  * { box-sizing: border-box; margin: 0; padding: 0; }
  html, body { width: 1200px; height: 904px; overflow: hidden; }
  body {
    background: var(--backdrop);
    font-family: "Saira", sans-serif;
    color: var(--ink);
    position: relative;
  }
  .card {
    position: absolute;
    left: 280px;
    width: 640px;
    height: 366px;
    background: var(--white);
    border-radius: 22px;
    overflow: hidden;
    box-shadow: 0 6px 18px rgba(0,0,0,.18);
  }
  .card--front { top: 52px; }
  .card--back { top: 486px; }

  .brand {
    position: absolute;
    left: 0; right: 0;
    text-align: center;
  }
  .brand__name {
    display: inline-flex;
    align-items: center;
    gap: 10px;
    font-weight: 800;
    font-size: 34px;
    letter-spacing: 2px;
    text-transform: uppercase;
    color: var(--ink);
  }
  .brand__dot {
    width: 14px; height: 14px;
    border-radius: 50%;
    background: var(--orange);
  }
  .rule {
    position: absolute;
    height: 3px;
    background: var(--orange);
  }
  .rule--thin { height: 2px; }

  /* Front */
  .front__decor {
    position: absolute;
    right: 0; top: 0;
    width: 260px; height: 210px;
    background: radial-gradient(circle at 70% 40%, var(--orange-soft), var(--grey-soft) 55%, var(--white) 85%);
    opacity: .8;
  }
  .front__brand { top: 100px; }
  .front__band {
    position: absolute;
    left: 0; right: 0; bottom: 0;
    height: 132px;
    background: var(--orange);
    border-top: 6px solid var(--white);
    box-shadow: 0 -3px 0 var(--ink);
    color: var(--white);
    text-align: center;
    padding-top: 22px;
  }
  .front__phone {
    display: inline-flex;
    align-items: center;
    gap: 10px;
    font-weight: 700;
    font-size: 30px;
    letter-spacing: 2px;
  }
  .front__tagline {
    margin-top: 10px;
    font-weight: 700;
    font-size: 19px;
    letter-spacing: 1px;
    text-transform: uppercase;
  }

  /* Back */
  .back__brand { top: 42px; }
  .services {
    position: absolute;
    list-style: none;
    font-weight: 500;
    font-size: 18px;
    line-height: 25px;
  }
  .services li { display: flex; align-items: center; gap: 12px; }
  .services li::before {
    content: "";
    width: 9px; height: 9px;
    background: var(--orange);
    flex: none;
  }
  .services--main { left: 44px; top: 112px; }
  .services--extra { left: 396px; top: 112px; }
  .back__band {
    position: absolute;
    left: 0; right: 0; bottom: 0;
    height: 92px;
    background: var(--orange);
    border-top: 5px solid var(--white);
    box-shadow: 0 -3px 0 var(--orange);
  }
  .contact {
    position: absolute;
    right: 40px; top: 18px;
    text-align right;
    text-align: right;
    color: var(--white);
    font-weight: 500;
    font-size: 19px;
    line-height: 26px;
  }
</style>
</head>
<body>

<section class="card card--front" aria-label="Card front">
  <div class="front__decor" role="img" aria-label="Faint saw blade and harbour bridge backdrop"></div>

  <div class="rule" style="left:60px; top:92px; width:520px;"></div>
  <div class="brand front__brand">
    <span class="brand__name"><span class="brand__dot"></span>Kestrelwood Carpentry</span>
  </div>
  <div class="rule" style="left:60px; top:160px; width:520px;"></div>
  <div class="rule rule--thin" style="left:90px; top:168px; width:460px;"></div>

  <div class="front__band">
    <div class="front__phone">
      <svg width="28" height="24" viewBox="0 0 28 24" aria-hidden="true">
        <path d="M3 8c0-4 6-6 11-6s11 2 11 6v2h-6V8H9v2H3z" fill="#fff"/>
        <rect x="6" y="12" width="16" height="10" rx="2" fill="#fff"/>
      </svg>
      0491570156
    </div>
    <div class="front__tagline">Anything carpentry, anywhere in Sydney</div>
  </div>
</section>

<section class="card card--back" aria-label="Card back">
  <div class="rule" style="left:30px; top:34px; width:580px;"></div>
  <div class="brand back__brand">
    <span class="brand__name" style="font-size:28px;"><span class="brand__dot" style="width:12px;height:12px;"></span>Kestrelwood Carpentry</span>
  </div>
  <div class="rule" style="left:30px; top:92px; width:580px;"></div>
  <div class="rule rule--thin" style="left:60px; top:100px; width:520px;"></div>

  <ul class="services services--main">
    <li>Decks and Peryolas</li>
    <li>Wall and Roof Farming</li>
    <li>Doors and Windows</li>
    <li>Attic Conversions</li>
    <li>Timber Flooring</li>
    <li>Extensions &amp; More</li>
  </ul>
  <ul class="services services--extra">
    <li>Shop Fitouts</li>
    <li>Refurbishments</li>
    <li>Fences/Gates</li>
    <li>Privacy Screens</li>
    <li>Cladding</li>
  </ul>

  <div class="back__band">
    <div class="contact">
      <div>Lic #-481903K</div>
      <div>kestrelwoodcarpentry@mailbox.com</div>
    </div>
  </div>
</section>

</body>
</html>
```